Flyer for annual KESTREL SUMMIT 2020

I would like a church event flyer designed. The event is called "KESTREL SUMMIT 2020". I am looking for a professional, yet catchy design that uses our brand colors and logo creatively while communicating key information of the event effectively.

1. The logo is attached in two color formats. The designer has the choice to use them as he/she want.

2. The location of the event is: Harlow Community Center, 239 Fennimore Street, Portland, ME 04117

3. Time and date of event. The designer can organize and format the date and time as he/she pleases.
Thursday December 31st @ 6:30PM
Friday January 1st @ 6:30PM
Saturday 2nd @ 6:30PM
Sunday 3rd @ 4:30PM

4. The topic of the event is "In Fire and On Fire". The designer is free to use this phrase as he/she pleases to create a good composition.

5. Speaker: Prophet Marcus Olunde (2 pictures of the speaker to choose from are attached)

6. Contact information: contact@brightmeadowfold.org - Telephone number: 207 583 2914

7. I would also like the following three words on the flyer. These words describe the focus of the event: FIRE, REVIVAL, PROPHETIC

Target Market(s)

Young adults

Font styles to use
Sans Serif

Requirements
Must have
• Logo, speaker's picture
Should not have
• cross image, church image

```html
<!DOCTYPE html>
<html lang="en">
<head>
<meta charset="utf-8">
<title>Kestrel Summit 2020 Flyer</title>
<link rel="stylesheet" href="https://fonts.googleapis.com/css2?family=Montserrat:wght@300;400;500;700;800&family=Roboto:wght@300;400;900&display=swap">
<style>
  :root {
    --navy: #03212f;
    --orange: #f6941e;
    --orange-text: #e8891f;
    --sky: #c2e1f3;
    --ink: #0d0d0d;
    --deep-blue: #0c3a5e;
    --white: #ffffff;
    --page: #ffffff;
  }
  * { margin: 0; padding: 0; box-sizing: border-box; }
  html, body {
    width: 1200px; height: 1200px; overflow: hidden;
    background: var(--page);
  }
  .canvas { position: relative; width: 1200px; height: 1200px; overflow: hidden; }
  .flyer {
    position: absolute; left: 172px; top: 0;
    width: 1231px; height: 1728px;
    transform: scale(0.6944); transform-origin: top left;
    background: var(--navy);
    font-family: "Montserrat", sans-serif;
    overflow: hidden;
  }
  .flyer-shapes { position: absolute; inset: 0; }
  .abs { position: absolute; white-space: nowrap; line-height: 1; }

  .brand { left: 46px; top: 120px; display: flex; align-items: center; gap: 18px; }
  .brand-dot { width: 26px; height: 26px; border-radius: 50%; background: var(--orange); }
  .brand-name { font-family: "Montserrat", sans-serif; font-weight: 500; font-size: 72px; color: var(--white); letter-spacing: 2px; }

  .theme { right: 45px; top: 146px; font-weight: 700; font-size: 48px; color: var(--deep-blue); }
  .theme .theme-and { font-weight: 400; font-size: 38px; }

  .title-main { right: 45px; top: 318px; font-weight: 800; font-size: 128px; color: var(--ink); letter-spacing: 2px; }
  .title-sub { right: 45px; top: 478px; font-weight: 800; font-size: 104px; color: var(--ink); letter-spacing: 1px; }
  .title-year { right: 45px; top: 612px; font-weight: 500; font-size: 118px; color: var(--navy); }

  .speaker-tag {
    position: absolute; left: 0; top: 1163px; width: 442px; height: 77px;
    background: var(--orange); padding: 10px 0 0 46px;
  }
  .speaker-label { font-size: 26px; font-weight: 400; color: var(--white); line-height: 1.2; }
  .speaker-name { font-size: 26px; font-weight: 700; color: var(--navy); line-height: 1.2; }

  .focus-words { left: 44px; top: 1318px; font-family: "Roboto", sans-serif; font-weight: 900; font-size: 100px; color: var(--orange-text); line-height: 1.12; white-space: normal; }
  .focus-words span { display: block; }

  .venue { right: 45px; top: 1004px; text-align: right; color: var(--white); font-size: 29px; line-height: 1.27; }
  .venue-name { font-weight: 700; }

  .schedule { right: 45px; top: 1272px; text-align: right; color: var(--white); font-size: 28px; }
  .schedule li { list-style: none; height: 48px; }
  .schedule b { font-weight: 700; }

  .contact { right: 45px; top: 1555px; text-align: right; color: var(--white); font-family: "Roboto", sans-serif; font-weight: 300; font-size: 24px; }
  .contact-row { display: flex; justify-content: flex-end; align-items: center; gap: 14px; height: 50px; }
  .icon { display: block; }
</style>
</head>
<body>
<div class="canvas">
  <div class="flyer">
    <svg class="flyer-shapes" width="1231" height="1728" viewBox="0 0 1231 1728">
      <defs>
        <linearGradient id="speakerTone" x1="0" y1="0" x2="0" y2="1">
          <stop offset="0" stop-color="#3a2a22"/>
          <stop offset="0.3" stop-color="#c6462a"/>
          <stop offset="1" stop-color="#d2512f"/>
        </linearGradient>
      </defs>
      <polygon points="786,0 1231,0 1231,683 739,918 0,402" fill="var(--orange)"/>
      <polygon points="0,402 739,918 0,1278" fill="var(--sky)"/>
      <polygon points="0,1278 1231,683 1231,1728 0,1728" fill="var(--navy)"/>
      <path role="img" aria-label="Photo of the speaker, Prophet Marcus Olunde, in an orange suit"
            d="M170,270 Q270,240 360,280 L420,560 Q480,620 490,700 L490,1041 L0,1278 L0,650 Q80,560 170,540 Z"
            fill="url(#speakerTone)"/>
    </svg>

    <div class="abs brand"><span class="brand-dot"></span><span class="brand-name">VERANTH</span></div>

    <div class="abs theme">IN FIRE <span class="theme-and">AND</span> ON FIRE</div>
    <div class="abs title-main">KESTREL</div>
    <div class="abs title-sub">SUMMIT</div>
    <div class="abs title-year">2020</div>

    <div class="speaker-tag">
      <div class="speaker-label">SPEAKER</div>
      <div class="speaker-name">PROPHET MARCUS OLUNDE</div>
    </div>

    <div class="abs focus-words"><span>FIRE</span><span>REVIVAL</span><span>PROPHETIC</span></div>

    <svg class="abs icon" style="left:1132px;top:912px" width="56" height="72" viewBox="0 0 56 72" aria-hidden="true">
      <path d="M28 69 C18 55 4 42 4 27 A24 24 0 0 1 52 27 C52 42 38 55 28 69 Z" fill="none" stroke="#fff" stroke-width="3"/>
      <circle cx="28" cy="27" r="10" fill="none" stroke="#fff" stroke-width="3"/>
    </svg>
    <div class="abs venue">
      <div class="venue-name">HARLOW COMMUNITY CENTER</div>
      <div>239 FENNIMORE STREET, PORTLAND</div>
      <div>ME 04117</div>
    </div>

    <svg class="abs icon" style="left:1120px;top:1184px" width="66" height="68" viewBox="0 0 66 68" aria-hidden="true">
      <rect x="6" y="12" width="57" height="53" rx="5" fill="none" stroke="#fff" stroke-width="3"/>
      <line x1="6" y1="28" x2="63" y2="28" stroke="#fff" stroke-width="3"/>
      <line x1="48" y1="4" x2="48" y2="18" stroke="#fff" stroke-width="3"/>
      <circle cx="20" cy="20" r="14" fill="var(--navy)" stroke="#fff" stroke-width="3"/>
      <path d="M20 12 V20 L26 24" fill="none" stroke="#fff" stroke-width="3"/>
      <g fill="#fff">
        <rect x="16" y="38" width="6" height="5"/><rect x="28" y="38" width="6" height="5"/><rect x="40" y="38" width="6" height="5"/><rect x="52" y="38" width="6" height="5"/>
        <rect x="16" y="50" width="6" height="5"/><rect x="28" y="50" width="6" height="5"/><rect x="40" y="50" width="6" height="5"/><rect x="52" y="50" width="6" height="5"/>
      </g>
    </svg>
    <ul class="abs schedule">
      <li><b>THURSDAY</b> DECEMBER 31ST @ 6:30PM</li>
      <li><b>FRIDAY</b> JANUARY 1ST @ 6:30PM</li>
      <li><b>SATURDAY</b> JANUARY 2ND @ 6:30PM</li>
      <li><b>SUNDAY</b> JANUARY 3RD @ 4:30PM</li>
    </ul>

    <div class="abs contact">
      <div class="contact-row">207 583 2914
        <svg class="icon" width="38" height="38" viewBox="0 0 38 38" aria-hidden="true">
          <path d="M8 4 L14 12 L10 16 Q14 24 22 28 L26 24 L34 30 L30 35 Q16 34 6 20 Q2 12 8 4 Z" fill="none" stroke="#fff" stroke-width="2.5"/>
          <path d="M22 10 A8 8 0 0 1 28 16 M23 4 A14 14 0 0 1 34 15" fill="none" stroke="#fff" stroke-width="2.5"/>
        </svg>
      </div>
      <div class="contact-row">CONTACT@BRIGHTMEADOWFOLD.ORG
        <svg class="icon" width="38" height="28" viewBox="0 0 38 28" aria-hidden="true">
          <rect x="2" y="3" width="34" height="22" fill="none" stroke="#fff" stroke-width="2.5"/>
          <path d="M2 3 L19 16 L36 3 M2 25 L14 13 M36 25 L24 13" fill="none" stroke="#fff" stroke-width="2.5"/>
        </svg>
      </div>
    </div>
  </div>
</div>
</body>
</html>
```